Zielgruppe
Wir sind ein kleines Restaurant in den schweizer Bergen. Unsere sonnige Terrasse mit bester Aussicht auf die umliegende Berglandschaft, läd zum verweilen und geniessen ein. Unser Publikum sind vor allem mehr oder weniger sportliche Schweizer jeden Alters, die auf ihrem Weg zu/von den umliegenden Wanderungen bei uns vorbei kommen, aber auch ältere Semester die nicht mehr so gut zu Fuß sind und deshalb auf der Terrasse verweilen. Auch Touristen kommen vorbei, wir sind für die aber mehr ein Geheimtipp. Am späten Nachmittag kommen ein paar Anwohner vorbei auf ein Feierabendgetränk und am Wochenende haben wir öfters die selben 'Einheimischen' hier für ein Mittagessen. Unser Angebot ist eher traditionell gehalten, aber wir wollen Gerichte anbieten die nicht auf jeder Hütte zu finden sind. Ich komme aus Tirol, meine Mitarbeiterin hier aus der Schweiz - deshalb haben wir einen Mix aus beiden Nationen auf den Tellern. Wir streben einen moderneren/coolen Stil an, der zu uns 'jungen Mädels' passt, der aber noch stark von Tradition und der Bergwelt geprägt ist. Unser Stübli ist sehr urig, aus dunkelm Holz gebaut und mit weissen Schaffellen und Kissen gemütlich gemacht. Die Einrichtung haben wir in den Farben weiss, dunkelrot und beige-brauntönen gehalten.
Aufgabenstellung
bitte nichts kitschiges oder zu buntes.
Die Masse 25x25 oder 26x26 gefallen uns am besten.
Der 'Hinweis' mit der MwSt und CHF sowie Kartenzahlung sollte bitte als kleine Fusszeile auf jeder Seite (ausser Titelseite und zweite Seite) sein

```html
<!DOCTYPE html>
<html lang="de">
<head>
<meta charset="utf-8">
<title>Was hei mer z'Ässe? – Suppen & Salat</title>
<link href="https://fonts.googleapis.com/css2?family=Bitter:ital,wght@0,400;0,700;1,400;1,700&family=Kaushan+Script&display=swap" rel="stylesheet">
<style>
  :root {
    --wood-dark: #2b2825;
    --wood-mid: #4a4540;
    --paper: #f0e2d6;
    --ink: #231f1c;
    --accent: #b97c3e;
    --white: #ffffff;
  }
  * { margin: 0; padding: 0; box-sizing: border-box; }
  html, body { width: 1200px; height: 1200px; overflow: hidden; }
  body { font-family: "Bitter", Georgia, serif; color: var(--ink); }

  .menu-page {
    position: relative;
    width: 1200px;
    height: 1200px;
    overflow: hidden;
  }
  .wood-background {
    position: absolute;
    inset: 0;
    background:
      linear-gradient(90deg, var(--wood-mid) 0%, var(--wood-dark) 12%, #3d3935 22%, #1f1d1b 30%, #45403b 45%, var(--wood-dark) 60%, #3f3a36 75%, #1e1c1a 82%, var(--wood-mid) 100%);
  }
  .page-title {
    position: absolute;
    left: 135px;
    top: 488px;
    transform: translate(-50%, -50%) rotate(-90deg);
    font-family: "Kaushan Script", cursive;
    font-size: 92px;
    line-height: 1;
    color: var(--white);
    white-space: nowrap;
  }
  .menu-card {
    position: absolute;
    left: 225px;
    top: 111px;
    width: 749px;
    height: 975px;
    background: var(--paper);
  }
  .section-title {
    position: absolute;
    left: 0; right: 0;
    text-align: center;
    font-family: "Kaushan Script", cursive;
    font-size: 56px;
    line-height: 1;
    color: var(--accent);
  }
  .line {
    position: absolute;
    left: 0; right: 0;
    text-align: center;
    line-height: 1;
    transform: translateY(-50%);
  }
  .dish-name { font-weight: 700; font-size: 23px; letter-spacing: 0.2px; }
  .dish-name .weight { font-weight: 400; }
  .dish-note { font-style: italic; font-size: 21px; }
  .dish-price { font-style: italic; font-weight: 700; font-size: 21px; color: var(--accent); }

  .divider {
    position: absolute;
    left: 176px;
    top: 528px;
    width: 400px;
    height: 10px;
  }
  .bowl-illustration {
    position: absolute;
    left: 306px;
    top: 790px;
    width: 190px;
    height: 136px;
    background: radial-gradient(ellipse at 45% 45%, #e8cfb6 0%, #dcb994 60%, var(--paper) 100%);
    border-radius: 40% 40% 50% 50%;
  }
</style>
</head>
<body>
<main class="menu-page">
  <div class="wood-background" role="img" aria-label="Dunkle Holzbretter als Hintergrund"></div>

  <h1 class="page-title">Was hei mer z'Ässe?</h1>

  <section class="menu-card">
    <h2 class="section-title" style="top:63px;">Eh Suppa</h2>

    <p class="line dish-name" style="top:150px;">Tagessuppe</p>
    <p class="line dish-note" style="top:177px;">täglich frisch im Stübli zubereitet aus saisonalen</p>
    <p class="line dish-note" style="top:204px;">Gemüsesorten</p>
    <p class="line dish-price" style="top:231px;">9,50</p>

    <p class="line dish-name" style="top:270px;">Tagessuppe mit einem Paar Rauchwürste</p>
    <p class="line dish-note" style="top:298px;">vom Metzger</p>
    <p class="line dish-price" style="top:324px;">18,50</p>

    <p class="line dish-name" style="top:364px;">Tagessuppe mit Alpkäse <span class="weight">(80g)</span></p>
    <p class="line dish-note" style="top:392px;">aus Sulwald</p>
    <p class="line dish-price" style="top:418px;">18,50</p>

    <p class="line dish-note" style="top:457px;">In der Bread-Bowl serviert</p>
    <p class="line dish-price" style="top:483px;">+ 4,00</p>

    <svg class="divider" viewBox="0 0 400 10" aria-hidden="true">
      <line x1="8" y1="5" x2="392" y2="5" stroke="#b97c3e" stroke-width="1.6"/>
      <circle cx="5" cy="5" r="3.6" fill="#f0e2d6" stroke="#b97c3e" stroke-width="1.4"/>
      <circle cx="395" cy="5" r="3.6" fill="#f0e2d6" stroke="#b97c3e" stroke-width="1.4"/>
    </svg>

    <h2 class="section-title" style="top:580px;">Epis Gsunds</h2>

    <p class="line dish-name" style="top:665px;">Kleiner grüner Salat,</p>
    <p class="line dish-note" style="top:693px;">serviert mit Brot</p>
    <p class="line dish-price" style="top:719px;">8,00</p>

    <div class="bowl-illustration" role="img" aria-label="Zeichnung einer Suppenschüssel mit Brotscheibe"></div>
  </section>
</main>
</body>
</html>
```